Kessa Lane Website Design

Need a website for a Dog Grooiming business. Please make it simular to these:

https://www.quorvatt.com
https://lintrevask.com
https://morvelandistel.com
https://www.pelthuvra.com/tensik/

```html
<!DOCTYPE html>
<html lang="en">
<head>
<meta charset="utf-8">
<title>Kessa Lane – Dog Grooming</title>
<link href="https://fonts.googleapis.com/css2?family=Mulish:wght@400;600;700;800&family=Oswald:wght@300;400&display=swap" rel="stylesheet">
<style>
:root{
  --purple:#7a3a8a;
  --purple-dark:#6a2f79;
  --green:#3b7d23;
  --green-dark:#2f6a1b;
  --text:#3a3a3a;
  --muted:#555;
  --grey-band:#ececee;
  --black:#0c0c0c;
  --white:#fff;
}
*{box-sizing:border-box;margin:0;padding:0}
html,body{width:1200px;height:4310px;overflow:hidden}
body{position:relative;font-family:'Mulish',sans-serif;color:var(--text);background:var(--white)}
.abs{position:absolute}
.btn{position:absolute;display:flex;align-items:center;justify-content:center;gap:8px;background:var(--green);color:var(--white);font-weight:700;font-size:14px;border:1px solid #fff3;text-decoration:none}
.btn.purple{background:var(--purple)}
.paw{width:22px;height:18px}
.section-title{position:absolute;left:0;width:1200px;text-align:center;font-weight:700;font-size:34px}
.section-title .p{color:var(--purple)}
.section-title .g{color:var(--green)}
.divider{position:absolute;left:562px;width:76px;height:3px}
.divider::before,.divider::after{content:"";position:absolute;top:0;height:2px;width:32px}
.divider::before{left:0;background:var(--purple)}
.divider::after{right:0;background:var(--green)}
.divider.light::before,.divider.light::after{background:#fff}

/* hero */
.hero{position:absolute;left:0;top:0;width:1200px;height:640px}
.hero-photo{position:absolute;inset:0;background:linear-gradient(100deg,#5d6b28 0%,#8a8f3c 35%,#b8a947 65%,#e0c86a 100%)}
.hero-pup{position:absolute;left:170px;top:140px;width:220px;height:470px;border-radius:40% 40% 20% 20%;background:radial-gradient(circle at 50% 40%,#f2ece4 0%,#d9c7b3 55%,transparent 75%)}
.logo{position:absolute;left:140px;top:28px;color:#fff;font-weight:700;font-size:34px;display:flex;align-items:center;gap:10px}
.logo .mark{width:28px;height:28px;border:3px solid #fff;border-radius:50%}
.nav{position:absolute;top:84px;left:570px;display:flex;gap:38px;font-size:14px;font-weight:600;color:#fff}
.nav span{position:relative}
.nav .active::after{content:"";position:absolute;left:50%;top:22px;width:8px;height:8px;margin-left:-4px;background:#fff;border-radius:50%}
.top-phone{position:absolute;left:862px;top:26px;display:flex;align-items:center;gap:10px;color:#fff;font-size:19px;font-weight:600}
.hero-head{position:absolute;left:408px;top:210px;width:305px;color:#fff;font-family:'Oswald',sans-serif;font-weight:300;font-size:32px;line-height:51px}
.quick{position:absolute;left:757px;top:211px;width:302px;height:352px;background:#fff;box-shadow:0 6px 18px rgba(0,0,0,.18)}
.quick-head{position:absolute;left:0;top:0;width:302px;height:72px}
.quick-head h3{position:absolute;left:0;top:12px;width:100%;text-align:center;color:#fff;font-size:22px;font-weight:700}
.field{position:absolute;left:17px;width:268px;height:30px;border:1px solid #ececec;font-size:11px;color:#444;padding:8px 13px}
.quick .btn{left:86px;top:304px;width:128px;height:38px;font-size:15px}

/* about */
.about-text{position:absolute;left:165px;top:758px;width:870px;text-align:center;font-size:13.5px;line-height:22.5px;color:var(--text)}
.about-text p+p{margin-top:12px}
.about-dog{position:absolute;left:1040px;top:915px;width:160px;height:177px;background:radial-gradient(circle at 55% 45%,#c78a45 0%,#e7c79c 45%,#f6efe6 75%,#fff 90%)}

/* services */
.services-bg{position:absolute;left:0;top:1092px;width:1200px;height:318px;background:linear-gradient(90deg,#3d3a2f,#5a4f3d 45%,#2e2a24)}
.services-sub{position:absolute;left:180px;top:1260px;width:840px;text-align:center;color:#f1f1f1;font-size:13.5px;line-height:23px}
.card{position:absolute;top:1352px;width:214px;height:398px;background:#fff;border:1px solid #ddd;box-shadow:0 2px 8px rgba(0,0,0,.12)}
.card .ph{position:absolute;left:7px;top:6px;width:200px;height:185px}
.card h4{position:absolute;left:0;top:210px;width:100%;text-align:center;color:var(--green);font-size:14px;font-weight:700;line-height:22px;padding:0 20px}
.card.first h4{color:var(--purple)}
.card p{position:absolute;left:0;top:264px;width:100%;text-align:center;font-size:12.5px;line-height:21px;padding:0 10px;color:var(--muted)}
.card .btn{left:0;top:370px;width:214px;height:28px;font-size:13px}

/* video */
.video{position:absolute;left:0;top:1925px;width:1200px;height:640px}
.video-photo{position:absolute;inset:0;background:linear-gradient(95deg,#4a4a50 0%,#6b6a70 40%,#8b8990 70%,#5c5a5e 100%)}

/* seen in */
.press{position:absolute;top:2722px;left:140px;width:920px;display:flex;justify-content:space-between;align-items:center;color:#1a1a1a}
.press span{font-size:34px;font-weight:800}
.press .light{font-weight:400}

/* reviews */
.reviews{position:absolute;left:0;top:2873px;width:1200px;height:617px;background:var(--grey-band)}
.review{position:absolute;top:3112px;width:433px;height:256px;background:#fff}
.review .bar{position:absolute;left:20px;bottom:-10px;width:393px;height:10px;background:var(--purple)}
.review h5{position:absolute;left:0;top:70px;width:100%;text-align:center;color:var(--green);font-size:15.5px;font-weight:700}
.review p{position:absolute;left:40px;top:124px;width:353px;text-align:center;font-size:12.5px;line-height:21.5px;color:var(--muted)}
.avatar{position:absolute;width:76px;height:76px;border-radius:50%;border:3px solid var(--green);background:radial-gradient(circle,#8aa07a,#5e7a4a);top:3080px}
.quote{position:absolute;right:14px;bottom:6px;font-size:44px;color:#ddd;font-weight:800;line-height:30px}
.arrow{position:absolute;top:3220px;width:22px;height:22px;border-radius:50%;background:#fff;display:flex;align-items:center;justify-content:center;box-shadow:0 0 0 2px #e8c84a}

/* cta */
.cta-text{position:absolute;left:255px;top:3600px;width:690px;text-align:center;font-size:21px;line-height:38px;color:#444}
.call{position:absolute;left:0;top:3728px;width:1200px;display:flex;justify-content:center;align-items:center;gap:14px}
.call .lbl{font-size:30px;color:#555}
.call .num{font-size:30px;font-weight:700;color:#111}
.cta-dog{position:absolute}

/* footer */
.footer{position:absolute;left:0;top:3940px;width:1200px;height:340px;background:var(--black);color:#fff}
.f-title{position:absolute;color:var(--green);font-size:14px;font-weight:600}
.f-title::after{content:"";position:absolute;left:0;top:24px;width:40px;height:2px;background:var(--green)}
.f-links{position:absolute;left:142px;top:108px;list-style:none;font-size:13px;line-height:28.5px;font-weight:600}
.f-hours{position:absolute;left:855px;top:112px;list-style:none;font-size:12px;line-height:17px}
.f-hours li{margin-bottom:14px;padding-left:14px;position:relative}
.f-hours li::before{content:"";position:absolute;left:0;top:7px;width:4px;height:4px;background:#fff;border-radius:50%}
.f-logo{position:absolute;left:428px;top:140px;color:var(--purple);font-size:40px;font-weight:700;display:flex;align-items:center;gap:12px}
.f-logo .mark{width:34px;height:34px;border:3px solid var(--purple);border-radius:50%}
.copy{position:absolute;left:0;top:4280px;width:1200px;height:30px;background:var(--green);color:#fff;font-size:11px}
.copy span{position:absolute;left:145px;top:9px}
.social{position:absolute;right:140px;top:5px;display:flex;gap:8px}
.social i{display:block;width:22px;height:22px;border:1.5px solid #fff;border-radius:50%}
</style>
</head>
<body>

<svg width="0" height="0" style="position:absolute">
  <defs>
    <symbol id="phone" viewBox="0 0 24 24"><path d="M6.6 10.8a15 15 0 006.6 6.6l2.2-2.2a1 1 0 011-.25 11.4 11.4 0 003.6.6 1 1 0 011 1V20a1 1 0 01-1 1A17 17 0 013 4a1 1 0 011-1h3.5a1 1 0 011 1c0 1.25.2 2.45.6 3.6a1 1 0 01-.25 1z" fill="currentColor"/></symbol>
    <symbol id="pawmark" viewBox="0 0 24 20"><circle cx="5" cy="7" r="2.4" fill="none" stroke="currentColor" stroke-width="1.5"/><circle cx="10" cy="4" r="2.4" fill="none" stroke="currentColor" stroke-width="1.5"/><circle cx="15" cy="4" r="2.4" fill="none" stroke="currentColor" stroke-width="1.5"/><circle cx="20" cy="7" r="2.4" fill="none" stroke="currentColor" stroke-width="1.5"/><path d="M12.5 9c3 0 6 4 6 7s-3 3-6 2-6 1-6-2 3-7 6-7z" fill="none" stroke="currentColor" stroke-width="1.5"/></symbol>
  </defs>
</svg>

<!-- HERO -->
<header class="hero">
  <div class="hero-photo" role="img" aria-label="Photo of a small terrier puppy running across a sunny lawn"></div>
  <div class="hero-pup" role="img" aria-label="Running puppy"></div>
  <svg class="abs" style="left:0;top:0" width="1200" height="640"><path d="M0,450 C150,520 250,640 380,625 C520,610 600,560 760,570 C950,580 1100,520 1200,460 L1200,640 L0,640 Z" fill="#fff"/></svg>
  <div class="logo"><span class="mark"></span>Kessa Lane</div>
  <a class="btn" style="left:703px;top:28px;width:140px;height:32px;font-size:13px"><svg class="paw" style="color:#fff"><use href="#pawmark"/></svg>Book Online</a>
  <div class="top-phone"><svg width="26" height="26" style="color:var(--purple)"><use href="#phone"/></svg>123.456.7890</div>
  <nav class="nav"><span class="active">Home</span><span>Grooming Services</span><span>About Us</span><span>FAQs</span><span>Contact Us</span></nav>
  <h1 class="hero-head">We Offer The Best Grooming Service In The Town And Have Very Attractive Rates</h1>
  <form class="quick">
    <svg class="quick-head" viewBox="0 0 302 72"><path d="M0,0 H302 V58 C220,44 180,72 151,72 C120,72 80,44 0,58 Z" fill="#7a3a8a"/></svg>
    <div class="quick-head"><h3>Quick Contact</h3></div>
    <div class="field" style="top:93px">Name</div>
    <div class="field" style="top:128px">Phone</div>
    <div class="field" style="top:162px">Service</div>
    <div class="field" style="top:200px;height:72px">Message</div>
    <a class="btn">Submit</a>
  </form>
</header>

<!-- ABOUT -->
<section>
  <h2 class="section-title" style="top:686px"><span class="p">About</span> <span class="g">Kessa Lane</span></h2>
  <div class="divider" style="top:740px"></div>
  <div class="about-text">
    <p>Lorem ipsum dolor sit amet, consectetuer adipiscing elit, sed diam nonummy nibh euismod tincidunt ut laoreet dolore magna aliquam erat volutpat. Ut wisi enim ad minim veniam, quis nostrud exerci tation ullamcorper suscipit lobortis nisl ut aliquip ex ea commodo consequat. Duis autem vel eum iriure dolor in hendrerit in vulputate velit esse molestie consequat, vel illum dolore eu feugiat nulla facilisis at vero eros et accumsan et iusto odio dignissim qui blandit praesent luptatum zzril delenit augue duis dolore te feugait nulla facilisi sse molestie cosse molestie co</p>
    <p>Lorem ipsum dolor sit amet, consectetuer adipiscing elit, sed diam nonummy nibh euismod tincidunt ut laoreet dolore magna aliquam erat volutpat. Ut wisi enim ad minim veniam, quis nostrud exerci tation.</p>
  </div>
  <a class="btn" style="left:474px;top:949px;width:117px;height:36px">Book Online</a>
  <a class="btn" style="left:618px;top:949px;width:107px;height:36px">Read More</a>
  <div class="about-dog" role="img" aria-label="Yorkshire terrier peeking in"></div>
</section>

<!-- SERVICES -->
<section>
  <div class="services-bg" role="img" aria-label="Groomer smiling while brushing a dog"></div>
  <h2 class="section-title" style="top:1183px;color:#fff">Dog Grooming Services</h2>
  <div class="divider light" style="top:1237px"></div>
  <p class="services-sub">Lorem Ipsum is simply dummy text of the printing and typesetting industry. Lorem Ipsum has been the industry's standard dummy text ever electronic typesetting, remaining essentially unchanged.</p>

  <article class="card first" style="left:142px">
    <div class="ph" role="img" aria-label="Golden retriever being bathed" style="background:linear-gradient(160deg,#e9e5df,#c89a5e)"></div>
    <h4>Bath With Shampoo &amp; Conditioner</h4>
    <p>Lorem ipsum dolor sit amet, consectetuer adipiscing elit, sed diam nonummy sum dolor sit amet, consectetuer adipi</p>
    <a class="btn purple">Read More</a>
  </article>
  <article class="card" style="left:377px">
    <div class="ph" role="img" aria-label="Papillon being trimmed" style="background:linear-gradient(160deg,#bfc6c9,#8a6a4e)"></div>
    <h4>Full Body Trimming/Styling</h4>
    <p>Lorem ipsum dolor sit amet, consectetuer adipiscing elit, sed diam nonummy sum dolor sit amet, consectetuer adipi</p>
    <a class="btn">Read More</a>
  </article>
  <article class="card" style="left:611px">
    <div class="ph" role="img" aria-label="Dog having its eyes cleaned" style="background:linear-gradient(160deg,#d7b08a,#9a6a40)"></div>
    <h4 style="top:220px">Ear &amp; Eye Cleaning</h4>
    <p>Lorem ipsum dolor sit amet, consectetuer adipiscing elit, sed diam nonummy sum dolor sit amet, consectetuer adipi</p>
    <a class="btn">Read More</a>
  </article>
  <article class="card" style="left:846px">
    <div class="ph" role="img" aria-label="Yorkshire terrier being brushed" style="background:linear-gradient(160deg,#c9d1cc,#a58a6c)"></div>
    <h4 style="top:218px">Combing/Brushing</h4>
    <p>Lorem ipsum dolor sit amet, consectetuer adipiscing elit, sed diam nonummy sum dolor sit amet, consectetuer adipi</p>
    <a class="btn">Read More</a>
  </article>

  <a class="btn" style="left:525px;top:1788px;width:183px;height:40px;font-size:16px"><svg class="paw" style="color:#fff"><use href="#pawmark"/></svg>Book Online</a>
</section>

<!-- VIDEO -->
<section class="video">
  <div class="video-photo" role="img" aria-label="Groomer blow-drying a white poodle on a grooming table"></div>
  <svg class="abs" style="left:0;top:0" width="1200" height="640">
    <circle cx="580" cy="260" r="48" fill="none" stroke="#fff" stroke-width="5"/>
    <path d="M566,232 L604,260 L566,288 Z" fill="#fff"/>
    <path d="M0,469 C100,575 200,635 320,628 C500,612 620,555 800,565 C1000,575 1120,515 1200,475 L1200,640 L0,640 Z" fill="#fff"/>
  </svg>
</section>

<!-- AS SEEN IN -->
<section>
  <h2 class="section-title" style="top:2632px"><span class="p">As</span> <span class="g">Seen In</span></h2>
  <div class="divider" style="top:2686px"></div>
  <div class="press">
    <span>Halvery</span>
    <span>Morrow</span>
    <span>Dunecrest</span>
    <span>KTV Nine</span>
    <span class="light">Plinth</span>
  </div>
</section>

<!-- REVIEWS -->
<section>
  <div class="reviews"></div>
  <h2 class="section-title" style="top:2977px"><span class="p">Happy Customer</span> <span class="g">Reviews</span></h2>
  <div class="divider" style="top:3031px"></div>

  <article class="review" style="left:142px">
    <h5>Mira Holt, Company Name</h5>
    <p>Lorem Ipsum is simply dummy text of the printing and typesetting industry. Lorem Ipsum has been the industry's standard dummy text ever since the 1500s, when an unknown printer took a galley of type and scrambled it to make a type specimen book. It has survived.</p>
    <span class="quote">”</span>
    <div class="bar"></div>
  </article>
  <div class="avatar" style="left:319px" role="img" aria-label="Customer portrait with her dog"></div>

  <article class="review" style="left:624px">
    <h5 style="top:78px">Tobin Reyes , Company Name</h5>
    <p>Lorem Ipsum is simply dummy text of the printing and typesetting industry. Lorem Ipsum has been the industry's standard dummy text ever since the 1500s, when an unknown printer took a galley of type and scrambled it to make a type specimen book. It has survived.</p>
    <span class="quote">”</span>
    <div class="bar"></div>
  </article>
  <div class="avatar" style="left:803px" role="img" aria-label="Customer portrait with her dog"></div>

  <div class="arrow" style="left:131px"><svg width="8" height="10"><path d="M6,1 L2,5 L6,9" fill="none" stroke="#333" stroke-width="2"/></svg></div>
  <div class="arrow" style="left:1046px"><svg width="8" height="10"><path d="M2,1 L6,5 L2,9" fill="none" stroke="#333" stroke-width="2"/></svg></div>
</section>

<!-- CALL TO ACTION -->
<section>
  <div class="cta-dog" style="left:75px;top:3590px;width:150px;height:220px;background:radial-gradient(ellipse at 50% 50%,#f0e2cc 0%,#e4cba8 50%,#fff 72%)" role="img" aria-label="Labrador puppy raising a paw"></div>
  <div class="cta-dog" style="left:955px;top:3610px;width:185px;height:170px;background:radial-gradient(ellipse at 50% 50%,#c98a4a 0%,#e3b682 45%,#fff 72%)" role="img" aria-label="Puppy cuddling a kitten"></div>
  <p class="cta-text">All Kessa Lane pet stylists have years of experience in complex grooming, dog safety and breed specific haircuts so we can ensure your fur babies will feel right at home with us</p>
  <div class="call"><span class="lbl">Call Us Today</span><svg width="40" height="40" style="color:#1f5f9a"><use href="#phone"/></svg><span class="num">123.456.7890</span></div>
  <a class="btn" style="left:478px;top:3790px;width:185px;height:38px;font-size:16px"><svg class="paw" style="color:#fff"><use href="#pawmark"/></svg>Book Online</a>
</section>

<!-- FOOTER -->
<footer class="footer">
  <div class="f-title" style="left:142px;top:68px">Quick Links</div>
  <ul class="f-links"><li>Home</li><li>Grooming Services</li><li>About Us</li><li>FAQs</li><li>Contact Us</li></ul>
  <div class="f-logo"><span class="mark"></span>Kessa Lane</div>
  <a class="btn" style="left:396px;top:230px;width:142px;height:32px;font-size:13px"><svg class="paw" style="color:#fff"><use href="#pawmark"/></svg>Book Online</a>
  <div class="abs" style="left:555px;top:232px;display:flex;align-items:center;gap:10px;font-size:19px;font-weight:700"><svg width="28" height="28" style="color:var(--purple)"><use href="#phone"/></svg>123.456.7890</div>
  <div class="f-title" style="left:855px;top:72px">Office hours</div>
  <ul class="f-hours">
    <li>Mon - Tue - Wed - Fri<br>9:30 - 11:00 &amp; 16:00 - 19:00</li>
    <li>Thurs : 16:00 - 19:00</li>
    <li>Sat : 9:30 - 11:00</li>
    <li>Sunday - By Appointment Only</li>
  </ul>
</footer>
<div class="copy"><span>Copyright © 2021 Kessa Lane. All Rights Reserved.</span>
  <div class="social"><i></i><i></i><i></i><i></i></div>
</div>

</body>
</html>
```